Steady Crews: Keeping Staff from Drifting Away
Everyday People Guides for the Shopkeeper and Reluctant Personnel Lead
Steady Crews: Keeping Staff from Drifting Away - Books
Creative Brief
title: Everyday People Guides for the Shopkeeper and Reluctant Personnel Lead E-book covers: I'd also like two high-resolution JPG cover images (one front and one back), sized at 5.5" x 8.5" with all elements stopping within .5" of the page edge. A low-resolution version of each image must also be supplied for use in e-book format. These images will include: Front cover: • Image An eye-catching photo/illustration representing the topic of the book (managing costly employee turnover) • Book title Steady Crews: Keeping Staff from Drifting Away • Subtitle with icon Everyday People Guides for the Shopkeeper and Reluctant Personnel Lead, Book 1 • Tagline none • Author name Rosalind Pettigrew, SPHR Back cover: • Image Mugshot of author • Publisher name RTKV Publishing • Author blurb & image (may be inside book) • Barcode Leave space in lower right-hand corner for Bookvane to insert. • Book blurb If you're a small-business owner or entrepreneur thinking, "How in the world do I stop this organization's crazy turnover?" this e-book is for you. Steady Crews: Keeping Staff from Drifting Away by certified Human Resources consultant Rosalind Pettigrew provides simple tools for those thrown into the role of "accidental HR manager." Compiled as book one in Pettigrew's series, Everyday People Guides for the Shopkeeper and Reluctant Personnel Lead, it delivers quick access to critical, yet simple, techniques and processes to help you manage HR issues like recruitment/hiring, performance, and more. Filled with explanations and advice, worksheets and handy calculators, you'll find a solid foundation of information to help you manage your organization's HR issues... without the learning curve.
Books
Corporate executives in small businesses and entrepreneurs tasked with the role of managing Human Resources unexpectedly.
Book one cover art: • Book series icon • 2 high-resolution JPG files (1 front cover, 1 back cover) • 5.5" x 8.5" final size, with a .5" margin at all page edges • 2 low-res JPG files of the same front- and back-cover art for use in e-book format • Book title must be large enough to read in thumbnail size (like book thumbnails viewed on Bookvane) • Designer will need to procure: o Author mug shot (if not inside book) o Final book blurb for back cover o Book formatting specs from PrintHollow.com

```html
<!DOCTYPE html>
<html lang="en">
<head>
<meta charset="utf-8">
<title>Steady Crews: Keeping Staff from Drifting Away – Cover Set</title>
<link rel="stylesheet" href="https://fonts.googleapis.com/css2?family=Arimo:wght@400;700&display=swap">
<style>
  :root {
    --page-bg: #ffffff;
    --ink-dark: #2f2f2f;
    --ink-mid: #4a4a4a;
    --ink-soft: #3c3c3c;
    --back-top: #f6f6f6;
    --back-mid: #cfcfcf;
    --back-bottom: #8c8c8c;
    --front-top: #ffffff;
    --front-bottom: #f1f1f1;
    --spine-bg: #f7f7f7;
    --edge: #d4d4d4;
    --photo-a: #e4e6e8;
    --photo-b: #6f737a;
    --photo-c: #26282c;
  }
  * { margin: 0; padding: 0; box-sizing: border-box; }
  html, body {
    width: 1200px; height: 636px; overflow: hidden;
    background: var(--page-bg);
    font-family: "Arimo", Arial, sans-serif;
  }

  /* Full wrap: back, spine, front */
  .spread {
    position: absolute; left: 96px; top: 84px;
    width: 600px; height: 473px;
    display: flex;
    border: 1px solid var(--edge);
  }
  .back-cover {
    position: relative; width: 288px; height: 100%;
    background: linear-gradient(to bottom, var(--back-top) 0%, var(--back-mid) 55%, var(--back-bottom) 100%);
    padding: 26px 22px;
  }
  .back-blurb { font-size: 7px; line-height: 1.42; color: var(--ink-soft); }
  .back-blurb p + p { margin-top: 6px; }
  .publisher {
    position: absolute; left: 22px; bottom: 22px;
    font-size: 11px; color: #ffffff;
  }
  .spine {
    position: relative; width: 48px; height: 100%;
    background: var(--spine-bg);
    border-left: 1px solid var(--edge); border-right: 1px solid var(--edge);
    overflow: hidden;
  }
  .spine-text {
    position: absolute; left: 50%; top: 14px;
    writing-mode: vertical-rl; transform: translateX(-50%);
    white-space: nowrap; color: var(--ink-dark);
  }
  .spine-author { font-size: 10px; margin-bottom: 14px; }
  .spine-title { font-size: 11px; font-weight: 700; }

  /* Front cover (shared) */
  .front-cover {
    position: relative; height: 100%;
    background: linear-gradient(to bottom, var(--front-top) 0%, var(--front-bottom) 100%);
    overflow: hidden; text-align: center;
  }
  .front-cover .author-name { position: absolute; left: 0; right: 0; color: var(--ink-mid); }
  .front-cover .book-title { position: absolute; font-weight: 700; line-height: 1.1; color: var(--ink-dark); }
  .front-cover .subtitle { position: absolute; font-weight: 700; line-height: 1.25; color: var(--ink-mid); }
  .front-cover .cover-photo {
    position: absolute; left: 0; right: 0; bottom: 0;
    background: radial-gradient(ellipse at 50% 50%, var(--photo-a) 0%, var(--photo-b) 55%, var(--photo-c) 100%);
  }

  .spread .front-cover { width: 264px; }
  .spread .author-name { top: 28px; font-size: 10px; }
  .spread .book-title { left: 12px; right: 12px; top: 46px; font-size: 16px; }
  .spread .subtitle { left: 14px; right: 14px; top: 90px; font-size: 8px; }
  .spread .cover-photo { top: 150px; }

  /* Standalone front */
  .single-front {
    position: absolute; left: 773px; top: 96px;
    width: 320px; height: 451px;
    border: 1px solid var(--edge);
  }
  .single-front .author-name { top: 22px; font-size: 12px; }
  .single-front .book-title { left: 14px; right: 14px; top: 44px; font-size: 20px; }
  .single-front .subtitle { left: 18px; right: 18px; top: 98px; font-size: 9.5px; }
  .single-front .cover-photo { top: 160px; }
</style>
</head>
<body>
  <div class="spread">
    <section class="back-cover">
      <div class="back-blurb">
        <p>If you're a small-business owner or entrepreneur thinking, "How in the world do I stop this organization's crazy turnover?" this e-book is for you. Steady Crews: Keeping Staff from Drifting Away by certified Human Resources consultant Rosalind Pettigrew provides simple tools for those thrown into the role of "accidental HR manager."</p>
        <p>Compiled as book one in Pettigrew's series, Everyday People Guides for the Shopkeeper and Reluctant Personnel Lead, it delivers quick access to critical, yet simple, techniques and processes to help you manage HR issues like recruitment/hiring, performance, and more. Filled with explanations and advice, worksheets and handy calculators, you'll find a solid foundation of information to help you manage your organization's HR issues... without the learning curve.</p>
      </div>
      <div class="publisher">RTKV Publishing</div>
    </section>
    <section class="spine">
      <div class="spine-text">
        <span class="spine-author">Rosalind Pettigrew, SPHR</span>
        <span class="spine-title">Steady Crews: Keeping Staff from Drifting Away</span>
      </div>
    </section>
    <section class="front-cover">
      <div class="author-name">Rosalind Pettigrew, SPHR</div>
      <h1 class="book-title">Steady Crews: Keeping Staff from Drifting Away</h1>
      <div class="subtitle">Everyday People Guides for the Shopkeeper and Reluctant Personnel Lead<br>Book 1</div>
      <div class="cover-photo" role="img" aria-label="Photo of a cheerful young office team celebrating together around a laptop"></div>
    </section>
  </div>

  <section class="front-cover single-front">
    <div class="author-name">Rosalind Pettigrew, SPHR</div>
    <h2 class="book-title">Steady Crews: Keeping Staff from Drifting Away</h2>
    <div class="subtitle">Everyday People Guides for the Shopkeeper and Reluctant Personnel Lead<br>Book 1</div>
    <div class="cover-photo" role="img" aria-label="Photo of a cheerful young office team celebrating together around a laptop"></div>
  </section>
</body>
</html>
```